Website Makeover for Local small business Law Enforcement Vendor

We are a very small business (2-3 employees) that provides training and study products to police officers study for promotion exams, as well as other law enforcement training. We currently use NestHarbor as our hosting company and we use one of there template makers for our web design. So your design will have to be compatible and easy for a novice to upload in place of the current NestHarbor template. This is vital. You will need to provide detailed instructions on how to convert your design to our existing website.

The website has an accompanying web store were customers can buy products, ultimately we'd like a full integration between the main website and the on-line store. However, we can't afford to have our site or store down for any period of time.

Our web address is www.trelvanrankprep.us It is simple and unprofessional. We'd like it to be modern and inviting.

We have four main categories of services/products:

1. Police Promotion Exam Preparation
2. Police Training
3. Police Entrance Exam Services
4. Police Department Services

We are open to your expertise and suggestions. We don't have many photos/graphics to offer you.
Updates

Target Market(s)

Police officers and Police Departments

Industry/Entity Type

Small Business

Requirements
Must have
• Easy conversion to existing NestHarbor hosting - with detailed instructions.

Link to our webstore - unless you can better integrate to existing site.

The ability for a novice to modify content and load updates with ease.
Nice to have
• The ability to post PDF's and/or Word documents for download by others (registration forms etc.)

```html
<!DOCTYPE html>
<html lang="en">
<head>
<meta charset="utf-8">
<title>Trelvan Consulting</title>
<link rel="stylesheet" href="https://fonts.googleapis.com/css2?family=Arimo:wght@400;700&family=Raleway:wght@300;400&family=Tinos&display=swap">
<style>
:root{
  --navy:#0b2a6f;
  --blue:#1a5fc8;
  --blue-dark:#1450b0;
  --text:#333;
  --muted:#555;
  --page:#f4f5f6;
  --panel:#eceeef;
  --footer:#e6e6e6;
  --bar:#2b2b2b;
  --rule:#d6d6d6;
}
*{margin:0;padding:0;box-sizing:border-box}
html,body{width:816px;height:1200px;overflow:hidden}
body{position:relative;background:var(--page);font-family:"Arimo",Arial,sans-serif;color:var(--text)}
.abs{position:absolute}
.top-band{left:0;top:0;width:816px;height:8px;background:var(--navy)}
.brand{left:328px;top:34px;width:160px;text-align:center;display:flex;align-items:center;justify-content:center;gap:7px}
.brand-dot{width:14px;height:14px;border-radius:50%;background:var(--navy)}
.brand-name{font-size:17px;font-weight:700;color:var(--navy);letter-spacing:1px;line-height:1.15}
.search{left:630px;top:99px;width:138px;height:23px;border:1px solid #bbb;background:#fff;font-size:10px;color:#999;padding:5px 7px}
.search svg{position:absolute;right:8px;top:5px}
.nav{left:45px;top:134px;width:725px;height:30px;background:var(--blue);display:flex;align-items:center;justify-content:space-around;padding:0 24px 0 30px}
.nav a{color:#fff;text-decoration:none;font-size:9px;letter-spacing:1.3px;font-variant:small-caps;font-weight:700;text-transform:capitalize}
.nav a.current{text-decoration:underline}
.hero{left:45px;top:164px;width:725px;height:283px;background:linear-gradient(180deg,#b9c7d8 0%,#6e7f93 45%,#2d3540 100%)}
.hero-strip{left:45px;top:447px;width:725px;height:8px;background:var(--blue)}
.hero-title{left:420px;top:198px;width:340px;text-align:center;font-family:"Raleway",sans-serif;font-weight:300;font-size:37px;line-height:40px;letter-spacing:1px}
.hero-title .l1{color:#1a4fb8}
.hero-title .l2{color:#fff;font-size:39px}
.hero-btn{left:463px;top:290px;width:249px;height:32px;background:var(--blue);color:#fff;font-size:11.5px;text-align:center;line-height:32px;letter-spacing:.3px}
.about{left:6px;top:456px;width:786px;height:304px;background:var(--panel)}
.photo-frame{left:92px;top:498px;width:214px;height:164px;background:#fff;box-shadow:0 3px 8px rgba(0,0,0,.2);padding:8px}
.photo-frame div{width:100%;height:100%;background:linear-gradient(180deg,#9a8a78 0%,#7a6d62 40%,#1d2330 70%,#2b2f38 100%)}
.about-title{left:333px;top:507px;font-size:13px;color:var(--blue);letter-spacing:.3px}
.about-lead{left:333px;top:530px;width:381px;font-size:9.6px;line-height:16px;text-align:justify;color:#222}
.about-body{left:333px;top:610px;width:381px;font-size:9px;line-height:16px;text-align:justify;color:var(--muted)}
.btn{top:669px;height:33px;color:#fff;font-size:10px;display:flex;align-items:center;justify-content:center;gap:8px;letter-spacing:.3px}
.btn-about{left:334px;width:191px;background:var(--blue)}
.btn-store{left:529px;width:191px;background:#3b3b3b}
.card{top:781px;width:170px}
.card-photo{height:116px;border-top:3px solid var(--blue)}
.card h3{margin-top:11px;font-weight:400;font-size:13px;line-height:13px;color:var(--blue);text-transform:uppercase;letter-spacing:.2px}
.card p{margin-top:7px;font-size:9.6px;line-height:13px;color:var(--muted);text-align:justify;height:39px}
.card .more{display:block;margin:6px 0 0 1px;width:96px;height:20px;background:var(--blue);color:#fff;font-family:"Tinos",serif;font-size:10.5px;text-align:center;line-height:20px}
.card .rule{margin-top:18px;height:3px;background:var(--rule)}
.footer{left:0;top:1056px;width:816px;height:120px;background:var(--footer)}
.story-title{left:62px;top:1068px;font-size:13px;color:#333}
.quote{font-family:"Tinos",serif;font-size:50px;color:#cfcfcf;line-height:1}
.story{left:64px;top:1088px;width:282px;font-size:9.4px;line-height:13px;color:#555}
.read-link{left:65px;top:1132px;font-size:9.6px;color:var(--blue)}
.addr{left:419px;top:1082px;font-size:9.8px;line-height:14px;color:#555}
.contact{left:614px;top:1082px;font-size:9.8px;line-height:14px;color:#444}
.social{top:1132px;width:24px;height:24px;border-radius:50%}
.copy{left:0;top:1176px;width:816px;height:24px;background:var(--bar);color:#ddd;font-size:8.5px;padding:6px 0 0 66px}
</style>
</head>
<body>
<div class="abs top-band"></div>

<div class="abs brand"><span class="brand-dot"></span><span class="brand-name">TRELVAN<br>CONSULTING</span></div>

<div class="abs search">Search
  <svg width="12" height="12" viewBox="0 0 12 12"><circle cx="4.5" cy="4.5" r="3.3" fill="none" stroke="#1a5fc8" stroke-width="1.6"/><line x1="7" y1="7" x2="11" y2="11" stroke="#1a5fc8" stroke-width="2"/></svg>
</div>

<nav class="abs nav">
  <a class="current">Home</a><a>About us</a><a>Department Services</a><a>Police Promotions</a><a>Police Employment</a><a>Free Resources</a>
</nav>

<div class="abs hero" role="img" aria-label="Close-up of a police cruiser with roof light bar"></div>
<div class="abs hero-strip"></div>
<div class="abs hero-title"><div class="l1">EXCEL WITH</div><div class="l2">EXCELLENCE</div></div>
<div class="abs hero-btn">VIEW UPCOMING COURSES SCHEDULE</div>

<div class="abs about"></div>
<div class="abs photo-frame"><div role="img" aria-label="Group of uniformed police officers standing before a stone wall"></div></div>
<h2 class="abs about-title" style="font-weight:400">ABOUT TRELVAN CONSULTANCY</h2>
<p class="abs about-lead">Trelvan Consulting LLC was founded by Marcus Trelvan. Marcus is a police lieutenant for a mid-sized police department in the greater Boston area. Marcus used a technique of memorization used by many students throughout the world to master the promotional material - the flash card memorization method.</p>
<p class="abs about-body">Millions of students have used flash cards to quickly and easily memorize large amounts of data in a short period of time. Law students, medical students, and students learning foreign languages have successfully used flash cards to learn difficult material.</p>
<div class="abs btn btn-about">
  <svg width="10" height="11" viewBox="0 0 10 11"><path d="M5 0.5 L9 2.5 V5.5 C9 8 7 9.8 5 10.5 C3 9.8 1 8 1 5.5 V2.5 Z" fill="none" stroke="#fff" stroke-width="1.3"/></svg>
  READ MORE ABOUT US</div>
<div class="abs btn btn-store">
  <svg width="13" height="11" viewBox="0 0 13 11"><path d="M0.5 1 H2.5 L4 7 H11 L12 3 H3" fill="none" stroke="#fff" stroke-width="1.2"/><circle cx="5" cy="9.3" r="1" fill="#fff"/><circle cx="10" cy="9.3" r="1" fill="#fff"/></svg>
  VIEW OUR ONLINE STORE</div>

<section class="abs card" style="left:41px">
  <div class="card-photo" role="img" aria-label="Officers signing documents at a table" style="background:linear-gradient(160deg,#4a4e58,#1b1e26 60%,#8a8478)"></div>
  <h3>Police Promotional Preparation</h3>
  <p>We have quickly become the leader in Police Promotional Preparation in Massachusetts.</p>
  <span class="more">read more</span><div class="rule"></div>
</section>
<section class="abs card" style="left:228px">
  <div class="card-photo" role="img" aria-label="Row of officers in dress uniform at a ceremony" style="background:linear-gradient(170deg,#7f8590,#15182a 55%,#2a2d3a)"></div>
  <h3>Police Employment Preparation</h3>
  <p>Exam preparation, interviewing &amp; assessment centers, career path and job search</p>
  <span class="more">read more</span><div class="rule"></div>
</section>
<section class="abs card" style="left:416px">
  <div class="card-photo" role="img" aria-label="Instructor demonstrating a training drill in a gym" style="background:linear-gradient(180deg,#a8aab0 0%,#5d6170 50%,#3a4fa8 100%)"></div>
  <h3>Police Training &amp; Education</h3>
  <p>Advanced &amp; Specialized legal training for State, Municipal and Campus Police....</p>
  <span class="more">read more</span><div class="rule"></div>
</section>
<section class="abs card" style="left:602px">
  <div class="card-photo" role="img" aria-label="Officers and staff standing outdoors under a pavilion" style="background:linear-gradient(180deg,#8c7a66 0%,#6a7a5a 45%,#24262e 100%)"></div>
  <h3>Law Enforcement Agency Services</h3>
  <p>Training, Entrance and Promotional Exam creation and administration, Assessment Centers and....</p>
  <span class="more">read more</span><div class="rule"></div>
</section>

<footer class="abs footer"></footer>
<span class="abs quote" style="left:52px;top:1066px">&ldquo;</span>
<span class="abs quote" style="left:310px;top:1108px">&rdquo;</span>
<h4 class="abs story-title" style="font-weight:400">Success Stories</h4>
<p class="abs story">Hello Marcus:&nbsp; In case you don't remember me:&nbsp;&nbsp; I took several of your seminars and bought mucho materials from you a couple years ago while studying for the LT exam in Millbrook.</p>
<span class="abs read-link">Read more &gt;</span>

<svg class="abs" style="left:388px;top:1081px" width="22" height="20" viewBox="0 0 22 20"><path d="M11 1 L21 10 H18 V19 H4 V10 H1 Z" fill="#cfcfcf"/></svg>
<div class="abs addr">Trelvan Consulting, LLC<br>P.O. Box 517<br>Ashcombe, MA 01990</div>

<svg class="abs" style="left:583px;top:1082px" width="22" height="14" viewBox="0 0 22 14"><path d="M1 5 C1 1 21 1 21 5 L17 6 L16 4 H6 L5 6 Z" fill="#cfcfcf"/><rect x="4" y="7" width="14" height="7" rx="1" fill="#cfcfcf"/></svg>
<svg class="abs" style="left:585px;top:1111px" width="18" height="12" viewBox="0 0 18 12"><rect x="0" y="0" width="18" height="12" fill="#cfcfcf"/><path d="M0 0 L9 7 L18 0" fill="none" stroke="#e6e6e6" stroke-width="1.2"/></svg>
<div class="abs contact">Tel:&nbsp; (555) 301-4482<br>Fax: (555) 301-4490<br>info@trelvanrankprep.us</div>
<span class="abs social" style="left:612px;background:#3556a0"></span>
<span class="abs social" style="left:642px;background:#ef8f1e"></span>

<div class="abs copy">Copyright &copy; 2013 Brightlane Studio</div>
</body>
</html>
```